Miriams Professional Resume

Pls upgrade to make look more effective and perhaps add α photo on it, both options with photo and without would be great. Thanks very much. I would also like the resume so I can edit as well if I need to down the track.

Target Market(s)

This is my professional resume to make it more effective to potential senior hiring managers,

Colors
f04a50

Requirements
Must have
• Professional look.

```html
<!DOCTYPE html>
<html lang="en">
<head>
<meta charset="utf-8">
<title>Miriam Holt – Resume</title>
<link rel="stylesheet" href="https://fonts.googleapis.com/css2?family=Arimo:wght@400;700&family=Open+Sans:ital,wght@0,400;0,700;1,400&display=swap">
<style>
:root{
  --red:#f04a50;
  --ink:#111111;
  --grey:#5e5e5e;
  --body:#222222;
  --bg:#35353a;
  --paper:#ffffff;
  --line:#f7a9ab;
}
*{margin:0;padding:0;box-sizing:border-box}
html,body{width:1200px;height:568px;overflow:hidden;background:var(--bg)}
.stage{position:relative;width:1200px;height:568px;font-family:"Arimo",Arial,sans-serif;color:var(--ink)}
.page{position:absolute;top:52px;width:329px;height:465px;background:var(--paper);overflow:hidden;box-shadow:0 6px 18px rgba(0,0,0,.45)}
.page--photo{left:73px}
.page--plain{left:434px}
.page--work{left:800px}
.abs{position:absolute}

/* header */
.portrait{left:22px;top:6px;width:60px;height:60px;border-radius:50%;border:1.5px solid var(--red);background:radial-gradient(circle at 50% 40%,#c9b3a8 0,#8a6f66 45%,#3b2f2e 100%)}
.name{font-weight:700;font-size:25px;letter-spacing:.3px;line-height:1;white-space:nowrap}
.name .last{color:var(--red)}
.page--photo .name{left:112px;top:14px}
.page--plain .name,.page--work .name{left:0;width:100%;text-align:center;color:var(--red);font-weight:400}
.page--plain .name{top:10px}
.page--work .name{top:8px;font-size:21px}
.page--plain .name .last,.page--work .name .last{font-weight:700}
.title{font-family:"Open Sans",sans-serif;font-size:6.4px;line-height:8px;text-align:center;white-space:nowrap}
.page--photo .title{left:124px;width:180px;top:41px}
.page--plain .title{left:0;width:100%;top:38px}
.title .years{color:var(--red)}

.tags{left:0;width:100%;height:15px;background:var(--red);color:#fff;font-weight:700;font-size:6px;display:flex;justify-content:center;gap:9px;align-items:center;white-space:nowrap}
.page--photo .tags{top:72px}
.page--plain .tags{top:72px}

.tab{left:0;width:74px;height:12px;border-radius:0 6px 6px 0;color:#fff;font-weight:700;font-size:7.6px;line-height:12px;padding-left:16px}
.page--photo .tab{background:var(--ink)}
.page--plain .tab{background:var(--red)}

.about{left:17px;width:298px;font-size:5.55px;line-height:7px;text-align:justify}
.about p{margin-bottom:7px}

.skills{left:16px;top:206px;width:302px;height:86px;border:0.7px solid var(--line);display:grid;grid-template-columns:1fr 1fr}
.skills ul{list-style:none;padding:3px 3px 0}
.skills ul+ul{border-left:0.7px solid var(--line)}
.skills li{height:15.6px;display:flex;align-items:center;justify-content:center;text-align:center;font-weight:700;font-size:4.6px;line-height:5.4px;border-bottom:0.7px dotted var(--red)}
.skills li:last-child{border-bottom:none}

.edu{left:16px;width:300px}
.edu-item{position:relative;padding-left:18px;height:21px;font-size:5.7px;line-height:7px}
.edu-badge{position:absolute;left:1px;top:1px;width:12px;height:12px;border-radius:50%;border:1px solid #c9c9c9}
.edu-badge--dark{background:#1d1d1d}
.edu-badge--gold{background:#d9a73a}
.edu-badge--blue{background:#2f7dc2}
.edu-item h3{font-size:5.7px;color:var(--red);font-weight:700}
.edu-item p{font-style:italic}
.edu-item p span{font-style:normal}
.sub{padding-left:18px;font-size:5.6px;line-height:7px;margin-top:2px}
.sub h4{color:var(--red);text-decoration:underline;font-size:5.8px;font-weight:700}
.sub li{list-style:none;padding-left:5px;position:relative}
.sub li::before{content:"";position:absolute;left:0;top:2.6px;width:2.2px;height:2.2px;border-radius:50%;background:var(--red)}
.sub+.sub{margin-top:6px}

.footer{left:0;top:435px;width:100%;height:30px;background:var(--red);color:#fff;font-weight:700;font-size:5.6px;display:flex;align-items:center;gap:16px;padding-left:17px;white-space:nowrap}
.contact{display:flex;align-items:center;gap:5px}
.contact-icon{width:9px;height:9px;border-radius:50%;background:var(--ink);display:flex;align-items:center;justify-content:center}
.page--plain .contact-icon{background:#fff}

/* work page */
.work-band{left:31px;top:37px;width:290px;height:9px;background:var(--red);color:#fff;font-weight:700;font-size:8.6px;line-height:9px;padding-left:7px}
.role-mark{left:7px;width:24px;height:24px;border-radius:50%;border:1px solid #e2e2e2;background:#fff;display:flex;align-items:center;justify-content:center}
.role-mark--solid{background:var(--red);border-color:var(--red);color:#fff;font-weight:700;font-size:5.4px}
.role-dot{width:10px;height:10px;border-radius:50%}
.role{left:39px;width:284px;font-family:"Open Sans",sans-serif;font-size:4.3px;line-height:5.95px;color:var(--body)}
.role h3{font-family:"Arimo",sans-serif;color:var(--red);font-size:5.4px;line-height:6.5px;font-weight:700}
.role .org{color:var(--grey);font-size:5.2px;line-height:6.5px;margin-bottom:6px}
.role .org i{font-style:italic}
.role ul{list-style:none}
.role li{position:relative;padding-left:4px}
.role li::before{content:"";position:absolute;left:0;top:2.2px;width:2px;height:2px;border-radius:50%;background:var(--red)}
.role--short .org{margin-bottom:0}
.work-rule{left:0;top:458px;width:100%;height:5px;background:var(--red)}
</style>
</head>
<body>
<div class="stage">

  <!-- Version with portrait -->
  <section class="page page--photo">
    <div class="abs portrait" role="img" aria-label="Portrait photo of Miriam Holt"></div>
    <h1 class="abs name">MIRIAM <span class="last">HOLT</span></h1>
    <p class="abs title">SENIOR MANAGER<br>ORGANISATIONAL DEVELOPMENT DIRECTOR<br><span class="years">(With 15 + years’ experience)</span></p>
    <div class="abs tags"><span># HR Strategy</span><span>#HR Daily Operations</span><span>#HR Projects</span><span>#Talent Management</span><span>#Business Solutions</span></div>

    <h2 class="abs tab" style="top:92px">ABOUT ME</h2>
    <div class="abs about" style="top:110px">
      <p>My strength is in leadership, developing strategies and providing excellence in HR Operational Services, Recruiting, People Development and building high performing teams to accelerate business performance and drive engagement.</p>
      <p>Masters in Strategic Organisational Development. As an authentic leader I excel at navigating across the business to build a positive culture while consulting with executives to understand imperative business needs and recommend the best solution.</p>
      <p>Successfully rolled out Brightfizz Project for 200 + new customer sites for the Orchid Fresh Fruit Project and actively recruited for 20 + technical field service agents, developed their capabilities and achieved 100% completion of the project.</p>
    </div>

    <h2 class="abs tab" style="top:187px">SKILL</h2>
    <div class="abs skills">
      <ul>
        <li>HUMAN RESOURCES STRATEGY</li>
        <li>HUMAN RESOURCES OPERATIONS</li>
        <li>RECRUITMENT PROCESS, TALENT ACQUISITION</li>
        <li>SINGAPORE, EMPLOYMENT LEGISLATION<br>&amp; INDUSTRIAL RELATIONS</li>
        <li>HR BUSINESS PARTNER</li>
      </ul>
      <ul>
        <li>HR POLICY</li>
        <li>CONSULTING, STAKEHOLDER MANAGEMENT</li>
        <li>TALENT MANAGEMENT, PERFORMANCE MANAGEMENT<br>COMPETENCY DEVELOPMENT</li>
        <li>AUSTRALIA, FAIR WORK,<br>NATIONAL STANDARDS &amp; AWARDS</li>
        <li>HR PROJECT MANAGEMENT</li>
      </ul>
    </div>

    <h2 class="abs tab" style="top:297px">EDUCATION</h2>
    <div class="abs edu" style="top:313px">
      <div class="edu-item"><span class="edu-badge edu-badge--dark"></span><h3>Masters in Strategic Organisational Development</h3><p>Northfield University, Australia <span>(December 2011 to December 2017)</span></p></div>
      <div class="edu-item"><span class="edu-badge edu-badge--gold"></span><h3>Management in Human Resources Certificate – Graduated with Distinction</h3><p>Coastal State University Extension Program, USA <span>(June 2003 – November 2006)</span></p></div>
      <div class="edu-item"><span class="edu-badge edu-badge--blue"></span><h3>Bachelor of Business in Tourism Management</h3><p>Eastport University, Australia <span>(January 1992 to December 1996)</span></p></div>
      <div class="sub"><h4>PROFESSIONAL MEMBERSHIPS</h4><ul><li>Member of Asia People Practice Institute, 102 3390 2020</li><li>Member of National People Leaders Institute, 374709.</li></ul></div>
      <div class="sub"><h4>CURRENT COURSES COMPLETED, 2020</h4><ul><li>Singapore Employment Legislation and Industrial Relations, APPI, 2020.</li><li>Human Resource Analytics and Insights, APPI, 2020.</li></ul></div>
    </div>

    <footer class="abs footer">
      <span class="contact"><span class="contact-icon"><svg width="5" height="4" viewBox="0 0 10 8"><rect x="0.5" y="0.5" width="9" height="7" fill="none" stroke="#f04a50" stroke-width="1.2"/><path d="M0.5 0.5 5 4.5 9.5 0.5" fill="none" stroke="#f04a50" stroke-width="1.2"/></svg></span>miriam@holtadvisory.example</span>
      <span class="contact"><span class="contact-icon"></span>https://profiles.example/miriam-holt-7b2</span>
    </footer>
  </section>

  <!-- Version without portrait -->
  <section class="page page--plain">
    <h1 class="abs name">MIRIAM <span class="last">HOLT</span></h1>
    <p class="abs title">SENIOR MANAGER<br>ORGANISATIONAL DEVELOPMENT DIRECTOR<br><span class="years">(With 15 + years’ experience)</span></p>
    <div class="abs tags"><span># HR Strategy</span><span>#HR Daily Operations</span><span>#HR Projects</span><span>#Talent Management</span><span>#Business Solutions</span></div>

    <h2 class="abs tab" style="top:92px">ABOUT ME</h2>
    <div class="abs about" style="top:110px">
      <p>My strength is in leadership, developing strategies and providing excellence in HR Operational Services, Recruiting, People Development and building high performing teams to accelerate business performance and drive engagement.</p>
      <p>Masters in Strategic Organisational Development. As an authentic leader I excel at navigating across the business to build a positive culture while consulting with executives to understand imperative business needs and recommend the best solution.</p>
      <p>Successfully rolled out Brightfizz Project for 200 + new customer sites for the Orchid Fresh Fruit Project and actively recruited for 20 + technical field service agents, developed their capabilities and achieved 100% completion of the project.</p>
    </div>

    <h2 class="abs tab" style="top:187px">SKILL</h2>
    <div class="abs skills">
      <ul>
        <li>HUMAN RESOURCES STRATEGY</li>
        <li>HUMAN RESOURCES OPERATIONS</li>
        <li>RECRUITMENT PROCESS, TALENT ACQUISITION</li>
        <li>SINGAPORE, EMPLOYMENT LEGISLATION<br>&amp; INDUSTRIAL RELATIONS</li>
        <li>HR BUSINESS PARTNER</li>
      </ul>
      <ul>
        <li>HR POLICY</li>
        <li>CONSULTING, STAKEHOLDER MANAGEMENT</li>
        <li>TALENT MANAGEMENT, PERFORMANCE MANAGEMENT<br>COMPETENCY DEVELOPMENT</li>
        <li>AUSTRALIA, FAIR WORK,<br>NATIONAL STANDARDS &amp; AWARDS</li>
        <li>HR PROJECT MANAGEMENT</li>
      </ul>
    </div>

    <h2 class="abs tab" style="top:297px">EDUCATION</h2>
    <div class="abs edu" style="top:313px">
      <div class="edu-item"><span class="edu-badge edu-badge--dark"></span><h3>Masters in Strategic Organisational Development</h3><p>Northfield University, Australia <span>(December 2011 to December 2017)</span></p></div>
      <div class="edu-item"><span class="edu-badge edu-badge--gold"></span><h3>Management in Human Resources Certificate – Graduated with Distinction</h3><p>Coastal State University Extension Program, USA <span>(June 2003 – November 2006)</span></p></div>
      <div class="edu-item"><span class="edu-badge edu-badge--blue"></span><h3>Bachelor of Business in Tourism Management</h3><p>Eastport University, Australia <span>(January 1992 to December 1996)</span></p></div>
      <div class="sub"><h4>PROFESSIONAL MEMBERSHIPS</h4><ul><li>Member of Asia People Practice Institute, 102 3390 2020</li><li>Member of National People Leaders Institute, 374709.</li></ul></div>
      <div class="sub"><h4>CURRENT COURSES COMPLETED, 2020</h4><ul><li>Singapore Employment Legislation and Industrial Relations, APPI, 2020.</li><li>Human Resource Analytics and Insights, APPI, 2020.</li></ul></div>
    </div>

    <footer class="abs footer">
      <span class="contact"><span class="contact-icon"><svg width="5" height="4" viewBox="0 0 10 8"><rect x="0.5" y="0.5" width="9" height="7" fill="none" stroke="#f04a50" stroke-width="1.2"/><path d="M0.5 0.5 5 4.5 9.5 0.5" fill="none" stroke="#f04a50" stroke-width="1.2"/></svg></span>miriam@holtadvisory.example</span>
      <span class="contact"><span class="contact-icon"></span>https://profiles.example/miriam-holt-7b2</span>
    </footer>
  </section>

  <!-- Work experience page -->
  <section class="page page--work">
    <h1 class="abs name">MIRIAM <span class="last">HOLT</span></h1>
    <div class="abs role-mark" style="top:29px"><span class="role-dot" style="background:var(--red)"></span></div>
    <h2 class="abs work-band">WORK EXPERIENCE</h2>

    <div class="abs role-mark role-mark--solid" style="top:57px">HAG</div>
    <article class="abs role" style="top:64px">
      <h3>Senior Manager, Organisational Development Director, Service, FMCG Industry</h3>
      <p class="org">Holt Advisory Group <i>(Singapore August 2015 to Present)</i></p>
      <ul>
        <li>Delivered HR Strategy &amp; Daily HR Operations, HR Policy, Recruitment, Performance Management &amp; Communications.</li>
        <li>Leadership, Team Management to 20 + Technical Field Service Agents, FMCG/ F &amp; B Retail Project.</li>
        <li>Recruitment Process for MNCs – Brightfizz, Crispo Chicken and Harbour Drinks for large scale projects.</li>
        <li>HR Advisor to business leaders to achieve business strategic objectives.</li>
        <li>Worked with Senior Leaders in manpower planning, skill development and tracking.</li>
        <li>Developed action plans and strategies to support business needs, talent management, performance management check ins.</li>
        <li>HRBP, Stakeholder Management, Workforce Planning for Orchid Fresh Project Roll Out.</li>
        <li>Project P + L Financial Management to $ 1.2 Million SG</li>
        <li>Digitalised business solution of online Service App, digitalised all services improvements to value add, increase efficiencies, transparency and reporting to customers.</li>
        <li>Provide tools required for Team Members and training on new Service App system.</li>
        <li>Manage Performance Management Process check ins, which resulted in greater levels of engagement</li>
        <li>Identify, source, interview, select the right talent to service 200 equipment assets/per month ie. 400+ field services performed each month and efficient operational call outs.</li>
        <li>Oversee weekly payroll and summary report. Sign off on PAYG Tax and GST Report</li>
        <li>Educated new hires on expected job tasks, compensation and benefits to set clear expectations.</li>
        <li>Coaching on expected behaviours through consultations, job spec and code of business reference.</li>
        <li>Project Management - resourcing &amp;operational requirements regards to the roll out of Brightfizz &amp; Crispo Chicken Technical Field Services for 200 equipment machines assets per month to deliver positive customer service results.</li>
      </ul>
    </article>

    <div class="abs role-mark" style="top:195px"><span class="role-dot" style="background:#1f3f8f"></span></div>
    <article class="abs role" style="top:203px">
      <h3>Organisational Development Director, Client Relations.</h3>
      <p class="org">Purewell Pty. Ltd <i>(Australia, June 2008 to August 2015)</i></p>
      <ul>
        <li>Established Business Strategy in consultation with management.</li>
        <li>Delivered HR Strategy and daily hands on Human Resources Operations:<br>Recruitment,Performance Management and Training and Development.</li>
        <li>Leadership to Team of 20 + resources, created a high performing service focused team.</li>
        <li>Client relations, effective communications and stakeholder management.</li>
        <li>Managed recruitment process for Equipment Field Services Team for Multi National Client Projects: Brightfizz, Crispo Chicken and Harbour Drinks.</li>
        <li>Recruit new Service Provider contracts with Brightfizz, Crispo Chicken, Burgerline and Harbour Drinks.</li>
        <li>Project P + L Financial Management to $ 1.2m SG</li>
        <li>Workforce Planning on Technical Field Projects for Brightfizz and Crispo Chicken for resources across NSW, QLD, VIC and SA for &gt; 200 services equipment assets, 400 + operational field services performed per month.</li>
        <li>Focused on quality service results, delivering a positive customer service experience.</li>
      </ul>
    </article>

    <div class="abs role-mark" style="top:290px"><span class="role-dot" style="background:#1aa0c8"></span></div>
    <article class="abs role" style="top:295px">
      <h3>Director Career Services.</h3>
      <p class="org">Westbay College <i>(USA, October 2003 to December 2007)</i></p>
      <ul>
        <li>Brand expansion, Business Development, Marketing of Westbay College into San Francisco, Sacramento, Fremont, Santa Clara and the Bay Area.</li>
        <li>Built out the department from scratch, developed strategies, process and service standards.</li>
        <li>HR Strategy and Human Resource Operations: Recruitment, Job Placement, Performance Management, HR Policy, Training and Development.</li>
        <li>Graduate Program Placement for 700 + Medical graduates, MA, LVN and RN Program.</li>
        <li>Acquired new accounts from multiple hospitals and medical centres across the San Francisco Bay Area.</li>
        <li>Project Management with Senior Leadership Team for Board of Private Education Accreditation Business Goal, engagement and contracts for preceptorships sites to facilitate L &amp; D.</li>
        <li>Awarded 2005 - Employee of the Year</li>
        <li>Account Management: Baycare Health, Hillview Medical Centre, Riverside Medical Centre and Service Veterans Support Office.</li>
      </ul>
    </article>

    <article class="abs role role--short" style="top:393px">
      <h3>Recruitment Consultant</h3>
      <p class="org">Meridian Staffing, Health Care and IT Industry <i>(Australia, July 2002 to April 2003)</i></p>
    </article>
    <article class="abs role role--short" style="top:413px">
      <h3>Recruitment Consultant</h3>
      <p class="org">Voltline, IT Industry <i>(Australia, July 2001 to May 2002)</i></p>
    </article>
    <article class="abs role role--short" style="top:433px">
      <h3>Sales and IT Sourcer</h3>
      <p class="org">Netarc Systems, IT Industry <i>(Australia, April 2000 to April 2001)</i></p>
    </article>
    <div class="abs work-rule"></div>
  </section>

</div>
</body>
</html>
```